Bref créative
Boréalis Soins Inc.
Business Cards, Stationnary and enveloppes
Professional
Mathis Lavoie
CFO
512-900 RUE CHAMPFLEURY
Québec, QC ,G2K 3B7
mlavoie@borealissoins-exemple.com
www.borealissoins-exemple.com
Boréalis Soins is a health agency for recruitment of human resources in health (nurse, pharmacist, doctors, etc.) for public and private services.
Boréalis is an emblematic bird of the Province of Québec and is synonym of dexterity, agility, precision, which are important in human care.
Logo + Web site

```html
<!DOCTYPE html>
<html lang="fr">
<head>
<meta charset="utf-8">
<title>Boréalis Soins — Papeterie</title>
<link rel="stylesheet" href="https://fonts.googleapis.com/css2?family=Open+Sans:wght@400;600;700&display=swap">
<style>
  :root{
    --bg:#e8e5e1;
    --paper:#ffffff;
    --red:#b3231c;
    --red-dark:#6a0e0b;
    --grey:#5b5b5b;
    --grey-light:#c9c9c9;
    --ink:#333333;
    --faint:#f1f1f1;
  }
  *{box-sizing:border-box;margin:0;padding:0}
  html,body{width:1200px;height:604px;overflow:hidden}
  body{background:var(--bg);font-family:"Open Sans",Arial,sans-serif;color:var(--ink);position:relative}
  .sheet,.envelope,.card{position:absolute;background:var(--paper);box-shadow:0 2px 6px rgba(0,0,0,.18);overflow:hidden}

  .brand{font-weight:700;text-transform:uppercase;letter-spacing:.06em;color:var(--grey);display:flex;align-items:center;gap:6px;white-space:nowrap}
  .brand .mark{width:10px;height:10px;background:var(--red)}
  .brand.on-red{color:#ffffff}
  .brand.on-red .mark{background:#ffffff}

  .sheet{width:384px;height:516px;top:44px}
  .fax{left:24px}
  .letterhead{left:432px}
  .sheet .brand{position:absolute;top:26px;left:26px;font-size:13px}
  .emblem-area{position:absolute;left:40px;top:200px;width:220px;height:220px;border-radius:50%;background:var(--faint)}
  .swoosh{position:absolute;left:0;bottom:0;width:100%;height:130px}
  .footer{position:absolute;z-index:2;left:26px;bottom:12px;display:grid;grid-template-columns:auto auto;column-gap:22px;row-gap:4px;font-size:6.5px;line-height:1.45;color:var(--grey);white-space:nowrap}

  .fax-title{position:absolute;top:58px;right:26px;font-size:15px;font-weight:700;font-style:italic;color:var(--red)}
  .fax-fields{position:absolute;top:84px;left:26px;right:26px;display:grid;grid-template-columns:1fr 1fr;column-gap:18px;row-gap:9px;font-size:7px;color:var(--grey)}
  .fax-fields span{display:block;border-bottom:1px solid var(--grey-light);padding-bottom:3px}
  .fax-checks{position:absolute;top:178px;left:26px;right:26px;display:flex;justify-content:space-between;font-size:6.5px;color:var(--grey)}
  .fax-checks span::before{content:"";display:inline-block;width:6px;height:6px;border:1px solid var(--grey);margin-right:3px;vertical-align:-1px}
  .fax-comments{position:absolute;top:202px;left:26px;font-size:7px;color:var(--grey)}

  .envelope{width:330px;height:136px;left:846px}
  .env-back{top:30px;background:var(--paper)}
  .env-back svg{position:absolute;inset:0;width:100%;height:100%}
  .env-front{top:184px}
  .env-front .brand{position:absolute;top:14px;left:16px;font-size:10px}
  .env-front .return{position:absolute;top:32px;left:16px;font-size:6px;line-height:1.4;color:var(--grey)}
  .env-front .window{position:absolute;left:16px;top:70px;width:140px;height:44px;border:1px solid var(--grey-light);border-radius:4px}
  .env-front .swoosh{height:60px}

  .card{width:170px;height:96px}
  .card-contact{left:846px;top:338px}
  .card-logo{left:1006px;top:338px;display:flex;align-items:center;justify-content:center}
  .card-back{left:846px;top:448px;background:linear-gradient(135deg,var(--red) 0%,var(--red-dark) 100%);display:flex;flex-direction:column;align-items:center;justify-content:center;gap:6px}
  .card-logo-2{left:1006px;top:448px;display:flex;flex-direction:column;align-items:center;justify-content:center;gap:6px}
  .card .brand{font-size:11px}
  .card-contact .brand{position:absolute;top:10px;left:10px;font-size:8px}
  .card-contact .person{position:absolute;z-index:2;top:28px;left:10px;font-size:7px;line-height:1.3;color:var(--grey);white-space:nowrap}
  .card-contact .person strong{color:var(--red);font-size:8px}
  .card-contact .swoosh{height:22px}
  .web{font-size:6px;color:var(--grey)}
  .card-back .web{color:#ffffff}
</style>
</head>
<body>

<section class="sheet fax">
  <div class="brand"><span class="mark"></span>Boréalis Soins</div>
  <div class="fax-title">Fax Sheet</div>
  <div class="fax-fields">
    <span>To:</span><span>From:</span>
    <span>Fax:</span><span>Pages:</span>
    <span>Phone:</span><span>Date:</span>
    <span>Re:</span><span>CC:</span>
  </div>
  <div class="fax-checks">
    <span>Urgent</span><span>For Review</span><span>Please Comment</span><span>Please Reply</span><span>Please Recycle</span>
  </div>
  <div class="fax-comments">Comments:</div>
  <div class="emblem-area" role="img" aria-label="Emblème Boréalis Soins en filigrane"></div>
  <svg class="swoosh" viewBox="0 0 384 130" preserveAspectRatio="none" aria-hidden="true">
    <path d="M0 130 L0 122 C150 116 280 80 384 10 L384 130 Z" fill="#ececec"/>
    <path d="M235 130 C300 110 350 70 384 26 L384 130 Z" fill="var(--grey)"/>
    <path d="M215 128 C290 106 345 62 384 18" fill="none" stroke="var(--red)" stroke-width="2"/>
  </svg>
  <div class="footer">
    <div>512-900 RUE CHAMPFLEURY<br>Québec, QC, G2K 3B7</div>
    <div>T 418 555-0142<br>F 418 555-0143</div>
    <div>mlavoie@borealissoins-exemple.com<br>www.borealissoins-exemple.com</div>
  </div>
</section>

<section class="sheet letterhead">
  <div class="brand"><span class="mark"></span>Boréalis Soins</div>
  <div class="emblem-area" role="img" aria-label="Emblème Boréalis Soins en filigrane"></div>
  <svg class="swoosh" viewBox="0 0 384 130" preserveAspectRatio="none" aria-hidden="true">
    <path d="M0 130 L0 122 C150 116 280 80 384 10 L384 130 Z" fill="#ececec"/>
    <path d="M235 130 C300 110 350 70 384 26 L384 130 Z" fill="var(--grey)"/>
    <path d="M215 128 C290 106 345 62 384 18" fill="none" stroke="var(--red)" stroke-width="2"/>
  </svg>
  <div class="footer">
    <div>512-900 RUE CHAMPFLEURY<br>Québec, QC, G2K 3B7</div>
    <div>T 418 555-0142<br>F 418 555-0143</div>
    <div>mlavoie@borealissoins-exemple.com<br>www.borealissoins-exemple.com</div>
  </div>
</section>

<section class="envelope env-back">
  <svg viewBox="0 0 330 136" preserveAspectRatio="none" aria-hidden="true">
    <defs>
      <linearGradient id="flap" x1="0" y1="0" x2="0" y2="1">
        <stop offset="0" stop-color="#c42a22"/>
        <stop offset="1" stop-color="#6a0e0b"/>
      </linearGradient>
    </defs>
    <path d="M0 136 L165 70 L330 136 Z" fill="#f4f4f4"/>
    <path d="M0 0 L330 0 L330 18 L180 86 Q165 92 150 86 L0 18 Z" fill="url(#flap)"/>
  </svg>
</section>

<section class="envelope env-front">
  <div class="brand"><span class="mark"></span>Boréalis Soins</div>
  <div class="return">512-900 RUE CHAMPFLEURY<br>Québec, QC, G2K 3B7</div>
  <div class="window"></div>
  <svg class="swoosh" viewBox="0 0 330 60" preserveAspectRatio="none" aria-hidden="true">
    <path d="M120 60 C220 52 290 30 330 4 L330 60 Z" fill="var(--grey)"/>
    <path d="M100 58 C210 48 285 22 330 0" fill="none" stroke="var(--red)" stroke-width="1.5"/>
  </svg>
</section>

<section class="card card-contact">
  <div class="brand"><span class="mark"></span>Boréalis Soins</div>
  <div class="person"><strong>Mathis Lavoie</strong><br>CFO<br>512-900 RUE CHAMPFLEURY<br>Québec, QC, G2K 3B7<br>mlavoie@borealissoins-exemple.com</div>
  <svg class="swoosh" viewBox="0 0 170 22" preserveAspectRatio="none" aria-hidden="true">
    <path d="M110 22 C140 18 158 10 170 2 L170 22 Z" fill="var(--grey)"/>
    <path d="M95 21 C132 16 155 7 170 0" fill="none" stroke="var(--red)" stroke-width="1.2"/>
  </svg>
</section>

<section class="card card-logo">
  <div class="brand"><span class="mark"></span>Boréalis Soins</div>
</section>

<section class="card card-back">
  <div class="brand on-red"><span class="mark"></span>Boréalis Soins</div>
  <div class="web">www.borealissoins-exemple.com</div>
</section>

<section class="card card-logo-2">
  <div class="brand"><span class="mark"></span>Boréalis Soins</div>
  <div class="web">www.borealissoins-exemple.com</div>
</section>

</body>
</html>
```